Professional Corporate Christmas Card

We require a Christmas card to send to corporate clients on behalf of our Accounting and Financial planning firm.
We like a clean design and our corporate colours are white, blue and silvery grey.
We don't want our logo on the front of the card. We would like something professional and elegant on the front, with the message 'Merry Christmas' or similar.
Our text for the inside of the card is:
Our very best wishes to you this festive season.
May 2014 bring you peace, joy and prosperity.
From the Directors and Staff at Dunmore Group of Companies.
We would like our logo to be subtly placed within the inside of the card - it could have a level of transparency if that helps to gain that effect. It could also be built into the design if you wish. I have attached the logo.
Our website is at http://dunmoregroup-example.com.au/ to give an idea of our corporate style.
**We will be printing through Printlane, so we would like the colours you use to be CYMK**
We will order the card size - 182x117cm (folded)
Thank you for considering the proposal ... we look forward to receiving your designs!
Target Market(s)
The audience of this card is varied: property developers, CEO's, cane farmers, professionals - it will be going to referral sources and our top end clients.
Industry/Entity Type
Printing

```html
<!DOCTYPE html>
<html lang="en">
<head>
<meta charset="utf-8">
<title>Dunmore Group of Companies – Season's Greetings</title>
<link rel="stylesheet" href="https://fonts.googleapis.com/css2?family=Pinyon+Script&family=Cinzel:wght@500&display=swap">
<style>
  :root {
    --paper: #ffffff;
    --ink: #16243d;
    --navy: #1d3a6b;
    --blue: #2f66a8;
    --sky: #8fb3dc;
    --silver: #c4cad3;
    --silver-light: #eef1f5;
    --silver-deep: #8e97a4;
  }
  html, body {
    margin: 0;
    padding: 0;
    overflow: hidden;
    background: var(--paper);
  }
  .card {
    position: relative;
    width: 1200px;
    height: 831px;
    background: var(--paper);
    overflow: hidden;
  }
  .festive-artwork {
    position: absolute;
    left: 0;
    top: 0;
    width: 1200px;
    height: 413px;
    background:
      radial-gradient(ellipse 440px 300px at 620px 230px, rgba(238,241,245,0.95), rgba(238,241,245,0) 70%),
      radial-gradient(ellipse 280px 220px at 360px 180px, rgba(143,179,220,0.75), rgba(143,179,220,0) 75%),
      linear-gradient(100deg, var(--navy) 0%, var(--blue) 20%, #9fb6d2 40%, var(--silver-light) 56%, var(--silver) 72%, var(--blue) 88%, var(--navy) 100%);
  }
  .front-greeting {
    position: absolute;
    top: 150px;
    left: 0;
    width: 1200px;
    margin: 0;
    text-align: center;
    font-family: "Pinyon Script", cursive;
    font-weight: 400;
    font-size: 96px;
    line-height: 1;
    color: var(--navy);
  }
  .brand-name {
    position: absolute;
    top: 62px;
    right: 120px;
    margin: 0;
    font-family: "Cinzel", serif;
    font-weight: 500;
    font-size: 42px;
    color: var(--paper);
    letter-spacing: 1px;
  }
  .greeting {
    position: absolute;
    top: 466px;
    left: 0;
    width: 1200px;
    margin: 0;
    text-align: center;
    font-family: "Pinyon Script", cursive;
    font-weight: 400;
    font-size: 66px;
    line-height: 80px;
    color: var(--ink);
  }
  .new-year-wish {
    position: absolute;
    top: 578px;
    left: 0;
    width: 1200px;
    margin: 0;
    text-align: center;
    font-family: "Cinzel", serif;
    font-weight: 500;
    font-size: 34px;
    line-height: 42px;
    text-transform: uppercase;
    color: var(--ink);
  }
  .sign-off {
    position: absolute;
    right: 75px;
    top: 700px;
    margin: 0;
    text-align: right;
    font-family: "Pinyon Script", cursive;
    font-size: 43px;
    line-height: 50px;
    color: var(--ink);
  }
  .company-name {
    position: absolute;
    right: 81px;
    top: 754px;
    margin: 0;
    font-family: "Cinzel", serif;
    font-weight: 500;
    font-size: 29px;
    line-height: 36px;
    text-transform: uppercase;
    color: var(--ink);
  }
  .silver-band {
    position: absolute;
    left: 0;
    bottom: 0;
    width: 1200px;
    height: 17px;
    background: linear-gradient(90deg, var(--silver-deep) 0%, var(--silver) 30%, var(--silver-light) 50%, var(--silver) 70%, var(--silver-deep) 100%);
  }
</style>
</head>
<body>
  <main class="card">
    <div class="festive-artwork" role="img" aria-label="Swirling blue and silver festive ribbon artwork"></div>
    <p class="front-greeting">Merry Christmas</p>
    <p class="brand-name">Dunmore</p>

    <h1 class="greeting">Our very best wishes to you this festive season</h1>
    <p class="new-year-wish">May 2014 bring you peace,<br>joy and prosperity</p>

    <p class="sign-off">From the Directors and Staff at</p>
    <p class="company-name">Dunmore Group of Companies</p>

    <div class="silver-band"></div>
  </main>
</body>
</html>
```